Brochure for Foot Care Products
Comfi-Toes Product Brochure
Project: Brochure for Foot Care Products
Brochure for Foot Care Products  - Personal Care
Creative Brief
Personal Care
Consumers (middle aged mostly). Business to Business Retailers
8 1/2 x 11 tri-fold brochure. 6 Panel, 4 color. Ready to print (please provide form that can be edited also)

```html
<!DOCTYPE html>
<html lang="en">
<head>
<meta charset="utf-8">
<title>Comfi-Toes Product Brochure</title>
<link href="https://fonts.googleapis.com/css2?family=Open+Sans:wght@400;600;700;800&family=Dancing+Script:wght@600&display=swap" rel="stylesheet">
<style>
:root{
  --green:#6aa43a;
  --green-dark:#4f8a2a;
  --charcoal:#3d3f41;
  --charcoal-deep:#2f3133;
  --paper:#ffffff;
  --canvas:#ededed;
  --ink:#4a4a4a;
  --muted:#8a8a8a;
  --sky:#8fb7d3;
  --sky-deep:#4f86ad;
}
*{box-sizing:border-box;margin:0;padding:0}
html,body{width:1200px;height:956px;overflow:hidden}
body{background:var(--canvas);font-family:"Open Sans",Arial,sans-serif;color:var(--ink);position:relative}
.spread{position:absolute;top:254px;width:580px;height:448px;display:flex;background:var(--paper);box-shadow:0 1px 4px rgba(0,0,0,.18)}
.spread--outside{left:14px}
.spread--inside{left:606px}
.panel{position:relative;flex:1;overflow:hidden;border-right:1px solid #e4e4e4}
.panel:last-child{border-right:none}
.copy{font-size:5.6px;line-height:1.5;margin-bottom:5px}
.wave{position:absolute;left:0;width:100%;display:block}

/* outside: company panel */
.company-mark{display:flex;align-items:center;gap:5px;padding:14px 12px 10px}
.company-mark .dot{width:16px;height:16px;border-radius:50%;background:var(--green)}
.company-mark .name{font-size:8px;font-weight:700;color:var(--green-dark);text-transform:uppercase;letter-spacing:.3px}
.panel--company .body{padding:0 12px}
.panel--company .footer{position:absolute;left:0;right:0;bottom:0;height:132px;background:var(--charcoal)}
.panel--company .footer .wave{top:-1px}
.statement{position:absolute;left:14px;right:12px;bottom:20px;color:#fff;font-size:7.6px;font-weight:700;line-height:1.4}

/* outside: maker panel */
.panel--maker .top{background:var(--charcoal);height:236px;padding:14px 12px;color:#e9e9e9}
.maker-mark{display:inline-flex;align-items:center;gap:5px;background:#fff;padding:4px 7px;margin-bottom:10px}
.maker-mark .sq{width:10px;height:10px;background:var(--green)}
.maker-mark .name{font-size:7.5px;font-weight:700;color:var(--green-dark)}
.panel--maker .wave{top:226px}
.origin{padding:32px 12px 0;text-align:center}
.origin-line{font-size:8px;font-weight:700;color:var(--charcoal)}
.origin-line strong{display:block;font-size:16px;color:var(--charcoal);margin-top:1px}
.origin-flag{display:block;width:38px;height:20px;margin:6px auto 8px;background:#d23a30}
.address{font-size:5.8px;line-height:1.6;color:var(--ink)}
.address b{font-weight:700}

/* outside: cover */
.panel--cover{background:var(--paper)}
.brand{display:flex;justify-content:flex-end;align-items:center;gap:5px;padding:12px 12px 0}
.brand .circle{width:16px;height:16px;border-radius:50%;background:var(--green)}
.brand .name{font-size:10px;font-weight:700;color:var(--green-dark)}
.tagline{text-align:center;font-size:8.6px;line-height:1.35;color:var(--green-dark);font-weight:600;padding:14px 18px 10px}
.product-lineup{margin:0 16px;height:64px;background:linear-gradient(180deg,#f5f7f8,#dfe4e7)}
.cover-photo{position:absolute;left:0;right:0;bottom:0;height:210px;background:linear-gradient(160deg,var(--sky) 0%,#c9dcea 45%,var(--sky-deep) 100%)}
.panel--cover .wave{top:226px}
.slogan{position:absolute;left:20px;right:10px;bottom:26px;font-family:"Dancing Script",cursive;font-size:14px;color:#fff;line-height:1.1;text-align:center}

/* inside */
.panel--catalog .band-top{height:26px;background:var(--green)}
.panel--catalog .wave--top{top:24px}
.panel--catalog .band-bottom{position:absolute;left:0;right:0;bottom:0;height:20px;background:var(--charcoal)}
.panel--catalog .wave--bottom{bottom:18px}
.catalog{padding:16px 10px 0}
.item{display:flex;gap:7px;margin-bottom:12px}
.item-photo{flex:0 0 50px;height:62px;background:linear-gradient(180deg,#f7f8f9,#d9dee2)}
.item-photo--wide{flex-basis:58px;height:48px}
.item-name{font-size:7.2px;font-weight:700;color:var(--green-dark);line-height:1.2}
.item-sub{font-size:5.6px;color:var(--muted);margin-bottom:3px}
.item .copy{margin-bottom:0;font-size:5.3px}
.item--stacked{display:block}
.item--stacked .item-photo{height:48px;margin-bottom:5px}
</style>
</head>
<body>

<section class="spread spread--outside" aria-label="Brochure outside">
  <article class="panel panel--company">
    <div class="company-mark"><span class="dot"></span><span class="name">Meadow Bath &amp; Body Co.</span></div>
    <div class="body">
      <p class="copy">Meadow Bath &amp; Body Co. is a family owned business offering gentle skin care made for everyday comfort at home.</p>
      <p class="copy">For more than twenty years we have listened to customers and built a range of lotions and creams that soothe, soften and protect tired skin.</p>
      <p class="copy">Every formula is tested for mildness and made in small batches so each jar you open is fresh and ready to use.</p>
      <p class="copy">Our team works with retailers and care providers to bring simple, honest products to people who need relief for their legs and feet.</p>
    </div>
    <div class="footer">
      <svg class="wave" viewBox="0 0 200 30" height="30" preserveAspectRatio="none" aria-hidden="true"><path d="M0 0H200V8C140 34 70 -6 0 22Z" fill="#fff"/><path d="M0 22C70 -6 140 34 200 8V13C140 38 70 0 0 27Z" fill="var(--green)"/></svg>
      <p class="statement">All our products are formulated with natural ingredients, free of irritating dyes and fragrances, phthalates, formaldehyde &amp; parabens.</p>
    </div>
  </article>

  <article class="panel panel--maker">
    <div class="top">
      <div class="maker-mark"><span class="sq"></span><span class="name">Northfield Care Corp</span></div>
      <p class="copy">Northfield Care Corp develops therapeutic skin care for clinics, pharmacies and families across the country.</p>
      <p class="copy">Our Comfi-Toes line was created with foot care nurses to ease dryness, cracked heels and daily discomfort.</p>
      <p class="copy">Each product is dermatologist reviewed and suitable for sensitive skin, including skin of people living with diabetes.</p>
      <p class="copy">For more information please visit us online or call our customer care line.</p>
    </div>
    <svg class="wave" viewBox="0 0 200 30" height="30" preserveAspectRatio="none" aria-hidden="true"><path d="M0 0H200V14C130 34 60 2 0 20Z" fill="var(--charcoal)"/><path d="M0 20C60 2 130 34 200 14V19C130 38 60 7 0 25Z" fill="var(--green)"/></svg>
    <div class="origin">
      <p class="origin-line">Developed and manufactured in <strong>Canada</strong></p>
      <span class="origin-flag" aria-hidden="true"></span>
      <p class="address"><b>Northfield Care Corp</b><br>412 Larchwood Avenue, Brampton, ON L6T 2K9<br>T: 905-555-0142 · F: 905-555-0143<br>www.northfieldcare.ca</p>
    </div>
  </article>

  <article class="panel panel--cover">
    <div class="brand"><span class="circle"></span><span class="name">Comfi-Toes</span></div>
    <p class="tagline">Therapeutic Skin Care Products<br>for the Daily Care of your Legs and Feet</p>
    <div class="product-lineup" role="img" aria-label="Row of Comfi-Toes product bottles and jars"></div>
    <div class="cover-photo" role="img" aria-label="Photo of relaxed bare feet against a soft blue sky"></div>
    <svg class="wave" viewBox="0 0 200 30" height="30" preserveAspectRatio="none" aria-hidden="true"><path d="M0 0H200V10C130 30 60 -4 0 16Z" fill="#fff"/><path d="M0 16C60 -4 130 30 200 10V15C130 35 60 1 0 21Z" fill="var(--green)"/></svg>
    <p class="slogan">If your feet are not happy,<br>you are not happy</p>
  </article>
</section>

<section class="spread spread--inside" aria-label="Brochure inside">
  <article class="panel panel--catalog">
    <div class="band-top"></div>
    <svg class="wave wave--top" viewBox="0 0 200 20" height="14" preserveAspectRatio="none" aria-hidden="true"><path d="M0 0H200V6C130 20 60 -2 0 12Z" fill="var(--green)"/></svg>
    <div class="catalog">
      <div class="item"><div class="item-photo" role="img" aria-label="Foam pump bottle"></div><div><p class="item-name">Comfi-Toes Foot Foam</p><p class="item-sub">Light daily moisture</p><p class="copy">A quick absorbing foam that softens rough skin and leaves feet feeling cool and fresh all day long.</p></div></div>
      <div class="item"><div class="item-photo" role="img" aria-label="Cream tube"></div><div><p class="item-name">Comfi-Toes Heel Balm</p><p class="item-sub">For cracked heels</p><p class="copy">Rich balm with shea butter to repair deep cracks and calluses. Apply twice daily for best results.</p></div></div>
      <div class="item"><div class="item-photo" role="img" aria-label="Spray bottle"></div><div><p class="item-name">Comfi-Toes Leg Spray</p><p class="item-sub">Refreshing relief</p><p class="copy">Cooling mist for tired legs after long days standing. Gentle enough for daily use on sensitive skin.</p></div></div>
    </div>
    <div class="band-bottom"></div>
    <svg class="wave wave--bottom" viewBox="0 0 200 20" height="14" preserveAspectRatio="none" aria-hidden="true"><path d="M0 20V10C60 -2 130 18 200 6V20Z" fill="var(--charcoal)"/></svg>
  </article>

  <article class="panel panel--catalog">
    <div class="band-top"></div>
    <svg class="wave wave--top" viewBox="0 0 200 20" height="14" preserveAspectRatio="none" aria-hidden="true"><path d="M0 0H200V12C140 -2 70 20 0 6Z" fill="var(--green)"/></svg>
    <div class="catalog">
      <div class="item item--stacked"><div class="item-photo" role="img" aria-label="Large cream jar"></div><p class="item-name">Comfi-Toes Foot Cream</p><p class="item-sub">Intensive care formula</p><p class="copy">Our best selling cream restores moisture to very dry feet with urea and natural oils, without a greasy feel.</p></div>
      <div class="item"><div class="item-photo item-photo--wide" role="img" aria-label="Lotion bottle"></div><div><p class="item-name">Comfi-Toes Body Lotion</p><p class="item-sub">All over comfort</p><p class="copy">Smooth lotion for legs, arms and hands that calms itching and protects skin through the seasons.</p></div></div>
      <div class="item"><div class="item-photo item-photo--wide" role="img" aria-label="Small tube"></div><div><p class="item-name">Comfi-Toes Toe Gel</p><p class="item-sub">Between the toes</p><p class="copy">Soothing gel that keeps skin dry and fresh between the toes.</p></div></div>
    </div>
    <div class="band-bottom"></div>
    <svg class="wave wave--bottom" viewBox="0 0 200 20" height="14" preserveAspectRatio="none" aria-hidden="true"><path d="M0 20V6C70 18 140 -2 200 10V20Z" fill="var(--charcoal)"/></svg>
  </article>

  <article class="panel panel--catalog">
    <div class="band-top"></div>
    <svg class="wave wave--top" viewBox="0 0 200 20" height="14" preserveAspectRatio="none" aria-hidden="true"><path d="M0 0H200V6C130 20 60 -2 0 12Z" fill="var(--green)"/></svg>
    <div class="catalog">
      <div class="item"><div class="item-photo" role="img" aria-label="Tall pump bottle"></div><div><p class="item-name">Comfi-Toes Soak</p><p class="item-sub">Warm water foot bath</p><p class="copy">Relaxing mineral soak that softens skin before care and eases aches after a long day.</p></div></div>
      <div class="item item--stacked"><div class="item-photo" role="img" aria-label="Wide tub of cream"></div><p class="item-name">Comfi-Toes Night Cream</p><p class="item-sub">Overnight repair</p><p class="copy">Apply before bed and wear cotton socks. Wake up to softer, smoother and visibly healthier feet. Fragrance free and gentle for daily use.</p></div>
    </div>
    <div class="band-bottom"></div>
    <svg class="wave wave--bottom" viewBox="0 0 200 20" height="14" preserveAspectRatio="none" aria-hidden="true"><path d="M0 20V10C60 -2 130 18 200 6V20Z" fill="var(--charcoal)"/></svg>
  </article>
</section>

</body>
</html>
```